36" inch (height) x 96" inch (width) Banner for Baseball Field

Hello. This project is an advertisement that will be printed onto a 3 foot by 8 foot full color banner and placed at little league fields in Southern California. A theme of the banner can be baseball. The company is my law office practicing Estate Planning and Tax Law. I am uploading the current business card, which has the logo, website, and telephone number. You can also pull images from www.rkpembrove.com I would like the banner to be a fun design that incorporates baseball somehow, but draws attention to my law and tax office, and my website. Please be creative, and have fun with it. The colors of my practice are included in the logo. At the bottom, it should say "Attorney Advertisement," but this can be in very small font in the bottom right or left corner.

Target Market(s)

Youth Baseball Fans

Industry/Entity Type

Law; Accounting

Colors

Designer to choose colors to be used in the design.

Requirements
Must have
• My telephone number. My website.
Nice to have
• Would like to see "Estate Planning" and "Tax Law and Preparation" Would also like to see "Attorney" and "CPA" or "Certified Public Accountant" prominently diplayed

```html
<!DOCTYPE html>
<html lang="en">
<head>
<meta charset="utf-8">
<title>RK Pembrove Law Offices – Field Banner</title>
<link href="https://fonts.googleapis.com/css2?family=Cinzel:wght@400;700&family=Montserrat:wght@700&family=PT+Serif:wght@700&family=Tinos:wght@700&display=swap" rel="stylesheet">
<style>
  :root {
    --backdrop: #e9ebee;
    --banner-white: #ffffff;
    --brand-blue: #1b93d3;
    --brand-grey: #939598;
    --sky-top: #6a5a8e;
    --sky-mid: #c98a86;
    --dusk-blue: #7f8fb0;
    --infield-dirt: #a9774f;
    --field-green: #4f7d3e;
    --field-deep: #3c6631;
  }
  * { margin: 0; padding: 0; box-sizing: border-box; }
  html, body { width: 800px; height: 1200px; overflow: hidden; background: var(--backdrop); }
  .canvas { position: relative; width: 800px; height: 1200px; }

  /* 96 x 36 in field banner, scaled to 760 x 285 */
  .banner {
    position: absolute; left: 20px; top: 457px; width: 760px; height: 285px;
    background: linear-gradient(120deg, #ffffff 0%, #f1f3f5 45%, #ffffff 62%, #eef0f2 100%);
    overflow: hidden; box-shadow: 0 4px 14px rgba(0,0,0,0.18);
  }
  .banner-art { position: absolute; inset: 0; }

  .firm-mark {
    position: absolute; left: 232px; top: 90px; width: 120px; height: 120px;
    display: flex; align-items: center; justify-content: center; text-align: center;
    font-family: 'Cinzel', serif; font-weight: 700; font-size: 16px; line-height: 1.2;
    color: var(--brand-blue);
  }

  .info { position: absolute; left: 390px; top: 0; width: 340px; height: 285px; }
  .office-lead {
    position: absolute; top: 16px; width: 100%; text-align: center;
    font-family: 'Cinzel', serif; font-weight: 400; font-size: 19px; letter-spacing: 1px;
    color: var(--brand-grey);
  }
  .office-of {
    position: absolute; top: 42px; left: 70px; width: 200px;
    display: flex; align-items: center; gap: 6px;
    font-family: 'Cinzel', serif; font-size: 11px; color: var(--brand-blue);
  }
  .office-of::before, .office-of::after { content: ""; flex: 1; height: 2px; background: var(--brand-blue); }
  .firm-name {
    position: absolute; top: 54px; width: 100%; text-align: center;
    font-family: 'Cinzel', serif; font-weight: 700; font-size: 34px; letter-spacing: 0.5px;
    color: var(--brand-blue); white-space: nowrap;
  }
  .contact-pill {
    position: absolute; left: 104px; top: 104px; width: 132px; height: 27px;
    border-radius: 8px; background: var(--brand-blue); color: var(--banner-white);
    font-family: 'Montserrat', sans-serif; font-weight: 700; font-size: 18px;
    display: flex; align-items: center; justify-content: center;
  }
  .phone {
    position: absolute; top: 134px; width: 100%; text-align: center;
    font-family: 'Tinos', serif; font-weight: 700; font-size: 44px; letter-spacing: -1px;
    color: var(--brand-grey); white-space: nowrap;
  }
  .web-lead {
    position: absolute; top: 192px; left: 20px; width: 300px;
    display: flex; align-items: center; gap: 6px;
    font-family: 'Montserrat', sans-serif; font-weight: 700; font-size: 10px; color: var(--brand-blue);
  }
  .web-lead::before, .web-lead::after { content: ""; flex: 1; height: 2px; background: var(--brand-blue); }
  .web-pill {
    position: absolute; left: 10px; top: 210px; width: 320px; height: 32px;
    border-radius: 11px; background: var(--brand-grey); color: var(--banner-white);
    font-family: 'PT Serif', serif; font-weight: 700; font-size: 17px; letter-spacing: 2px;
    display: flex; align-items: center; justify-content: center;
  }
  .disclaimer {
    position: absolute; top: 258px; right: 8px;
    font-family: 'Tinos', serif; font-weight: 700; font-size: 10px; color: var(--brand-blue);
  }
</style>
</head>
<body>
<div class="canvas">
  <div class="banner">
    <svg class="banner-art" width="760" height="285" viewBox="0 0 760 285" xmlns="http://www.w3.org/2000/svg">
      <defs>
        <linearGradient id="sceneTone" x1="0" y1="0" x2="0" y2="1">
          <stop offset="0" stop-color="var(--sky-top)"/>
          <stop offset="0.28" stop-color="var(--sky-mid)"/>
          <stop offset="0.45" stop-color="var(--dusk-blue)"/>
          <stop offset="0.6" stop-color="var(--field-green)"/>
          <stop offset="0.74" stop-color="var(--infield-dirt)"/>
          <stop offset="0.84" stop-color="var(--field-green)"/>
          <stop offset="1" stop-color="var(--field-deep)"/>
        </linearGradient>
      </defs>
      <path class="hero-photo" role="img" aria-label="Photo of a batter in pinstripes at the plate over a little league ballfield at sunset"
            d="M0,0 H320 Q250,150 340,285 H0 Z" fill="url(#sceneTone)"/>
      <path class="swoosh-band" d="M320,0 H352 Q282,150 374,285 H340 Q250,150 320,0 Z" fill="var(--brand-blue)"/>
      <circle class="mark-disc" cx="292" cy="150" r="62" fill="var(--banner-white)"/>
    </svg>

    <div class="firm-mark">RK<br>PEMBROVE</div>

    <div class="info">
      <p class="office-lead">THE LAW OFFICES</p>
      <p class="office-of">OF</p>
      <h1 class="firm-name">RK PEMBROVE</h1>
      <p class="contact-pill">Contact us</p>
      <p class="phone">(805) 555-0142</p>
      <p class="web-lead">Visit Our Website</p>
      <p class="web-pill">www.rkpembrove.com</p>
      <p class="disclaimer">Attorney Advertisement</p>
    </div>
  </div>
</div>
</body>
</html>
```